Catering company needs business cards

We need new business cards for growing catering company.

Industry/Entity Type

Business

Requirements
Must have
• Company logo
• Marisol Quedenfeldt
• Catering Director
• marisol.t.quedenfeldt-1@orvanta-mail.org
• 407-555-0182
• 407-555-0267
• Building R2-718 PTX
• Brightwater Launch Campus
• Florida, 33741

```html
<!DOCTYPE html>
<html lang="en">
<head>
<meta charset="utf-8">
<title>Clearwater Table Catering – Business Cards</title>
<link rel="stylesheet" href="https://fonts.googleapis.com/css2?family=Open+Sans:wght@400;600&display=swap">
<style>
  :root {
    --page-bg: #ececec;
    --card-bg: #ffffff;
    --brand-blue: #1f78c1;
    --brand-green: #5e9a2c;
    --ink-dark: #2f2f2f;
    --ink-light: #9a9a9a;
    --icon-tint-blue: #5a9fd6;
    --icon-tint-green: #8dbb63;
  }
  * { box-sizing: border-box; margin: 0; padding: 0; }
  html, body { width: 1200px; height: 856px; overflow: hidden; }
  body {
    background: var(--page-bg);
    font-family: "Open Sans", Arial, sans-serif;
    position: relative;
  }
  .card {
    position: absolute;
    left: 250px;
    width: 700px;
    height: 380px;
    background: var(--card-bg);
    border-radius: 44px;
    overflow: hidden;
    box-shadow: 0 4px 14px rgba(0,0,0,0.12);
  }
  .card--front { top: 28px; }
  .card--back { top: 448px; }
  .card__corners { position: absolute; inset: 0; width: 100%; height: 100%; }

  /* front */
  .brand-name {
    position: absolute;
    top: 96px; left: 130px; right: 130px;
    text-align: center;
    color: var(--brand-blue);
    font-weight: 600;
    font-size: 31px;
    letter-spacing: 0.5px;
    white-space: nowrap;
  }
  .holder {
    position: absolute;
    top: 190px; left: 130px; right: 130px;
    text-align: center;
  }
  .holder__name { color: var(--ink-dark); font-size: 27px; font-weight: 400; line-height: 1.15; }
  .holder__role { color: var(--ink-light); font-size: 14px; margin-top: 2px; }
  .holder__email { color: var(--ink-dark); font-size: 14px; margin-top: 30px; white-space: nowrap; }

  /* back */
  .services {
    position: absolute;
    top: 86px; left: 200px; width: 300px;
    color: var(--brand-green);
    font-size: 14px;
    line-height: 1.4;
    text-align: center;
  }
  .contact {
    position: absolute;
    top: 150px; left: 200px; width: 300px;
    color: var(--ink-dark);
    font-size: 14px;
    line-height: 1.5;
    text-align: center;
  }
</style>
</head>
<body>

  <section class="card card--front" aria-label="Business card front">
    <svg class="card__corners" viewBox="0 0 700 380">
      <path d="M0 0 H210 C120 40 70 140 50 380 H0 Z" fill="var(--brand-blue)"/>
      <path d="M700 60 C610 120 560 250 500 380 H700 Z" fill="var(--brand-green)"/>
      <rect x="28" y="100" width="56" height="90" rx="10" fill="var(--icon-tint-blue)" role="img" aria-label="Fork and knife icon"/>
      <rect x="610" y="70" width="62" height="90" rx="10" fill="var(--icon-tint-green)" role="img" aria-label="Fork and spoon icon"/>
    </svg>
    <div class="brand-name">Clearwater Table Catering</div>
    <div class="holder">
      <p class="holder__name">Marisol Quedenfeldt</p>
      <p class="holder__role">Catering Director</p>
      <p class="holder__email">marisol.t.quedenfeldt-1@orvanta-mail.org</p>
    </div>
  </section>

  <section class="card card--back" aria-label="Business card back">
    <svg class="card__corners" viewBox="0 0 700 380">
      <path d="M0 0 H170 C105 45 62 140 48 270 C30 276 12 280 0 282 Z" fill="var(--brand-blue)"/>
      <path d="M700 20 C640 90 610 200 540 300 C520 330 500 360 490 380 H700 Z" fill="var(--brand-green)"/>
      <rect x="22" y="90" width="48" height="80" rx="9" fill="var(--icon-tint-blue)" role="img" aria-label="Fork and knife icon"/>
      <rect x="600" y="80" width="58" height="86" rx="10" fill="var(--icon-tint-green)" role="img" aria-label="Fork and spoon icon"/>
    </svg>
    <div class="services">
      <p>Recipes | Salad | Quiche | Meat</p>
      <p>Side dish | Pancakes | brownies</p>
    </div>
    <div class="contact">
      <p>Building R2-718 PTX</p>
      <p>Brightwater Launch Campus</p>
      <p>Florida, 33741</p>
      <p>www.clearwatertable.com</p>
      <p>T 407-555-0182</p>
      <p>F 407-555-0267</p>
    </div>
  </section>

</body>
</html>
```